NEW Modern Sleek Business Card for VR Language Startup

Our startup is using VR to lead the next wave of world language education. We need a two-sided business card that introduces the larger organization (Quorvel Language Inc) and our contact info on one side and shows the product, Lumidrasca, on the other side.

Side 1 (contact info)= Quorvel Logo and Contact info (name, title, phone, email)

Side 2 (product)= Lumidrasc logo, text, and website
Text= Culturally Immersive Language Learning Games
Website= www.lumidrasc.example

Target Market(s)

Education, Technology

Contact Information for Business Card

Contact info will be updated upon approval of the design. For now, put this as a placeholder.

Perry Hollins
Founder & CEO
phollins@mailtrove.example
(555)-014-2736

Font styles to use
Other font styles liked:
• Gibson and Century Gothic are the brand fonts

Requirements
Nice to have
• I would love to see cohesion between the design and colors of the two logos. I have attached a few business card designs that I like, so you can get a feel for my preferred style.

```html
<!DOCTYPE html>
<html lang="en">
<head>
<meta charset="utf-8">
<title>Quorvel Language – Business Card</title>
<link rel="stylesheet" href="https://fonts.googleapis.com/css2?family=Roboto:wght@400;500;700&display=swap">
<style>
  :root {
    --backdrop: #2b2b2d;
    --card: #f1f1f1;
    --ink: #3a3a3a;
    --ink-soft: #5a5a5a;
    --brand-blue: #4a6ee0;
    --brand-teal: #3fb8d8;
    --accent-blue: #4a8fe6;
    --accent-orange: #e8702a;
    --rule: #6f86e8;
  }
  * { box-sizing: border-box; margin: 0; padding: 0; }
  html, body { width: 1200px; height: 992px; overflow: hidden; }
  body {
    background: var(--backdrop);
    font-family: "Roboto", Arial, sans-serif;
    position: relative;
  }
  .card {
    position: absolute;
    left: 220px;
    width: 760px;
    height: 434px;
    background: var(--card);
    box-shadow: 0 10px 30px rgba(0,0,0,.45);
  }
  .card--product { top: 42px; }
  .card--contact { top: 516px; }

  /* Product side */
  .product-brand {
    position: absolute;
    top: 120px; left: 0; right: 0;
    display: flex; align-items: center; justify-content: center; gap: 18px;
  }
  .brand-dot {
    width: 64px; height: 64px; border-radius: 50%;
    background: linear-gradient(135deg, var(--brand-teal), var(--brand-blue));
  }
  .product-name {
    font-size: 56px; font-weight: 500; color: var(--brand-blue);
    letter-spacing: 0.5px;
  }
  .product-tagline {
    position: absolute; top: 238px; left: 0; right: 0;
    text-align: center; font-size: 17px; font-weight: 500; color: var(--ink);
  }
  .product-web {
    position: absolute; top: 268px; left: 0; right: 0;
    display: flex; align-items: center; justify-content: center; gap: 10px;
  }
  .product-web svg { display: block; }
  .product-url { font-size: 17px; color: var(--brand-blue); }

  /* Contact side */
  .company-brand {
    position: absolute; top: 70px; right: 70px;
    display: flex; align-items: center; gap: 16px;
  }
  .company-dot {
    width: 56px; height: 56px; border-radius: 50%;
    background: linear-gradient(135deg, #f29a2e, #e2345f 55%, #6a4ee0);
  }
  .company-name {
    font-size: 40px; font-weight: 700; color: var(--ink);
    letter-spacing: 4px;
  }
  .contact {
    position: absolute; left: 64px; bottom: 60px;
  }
  .contact-name { font-size: 30px; font-weight: 500; color: var(--accent-blue); }
  .contact-title { font-size: 20px; font-weight: 500; color: var(--accent-orange); margin-top: 2px; }
  .contact-line { font-size: 18px; color: var(--ink-soft); margin-top: 8px; }
</style>
</head>
<body>
  <section class="card card--product" aria-label="Product side">
    <div class="product-brand">
      <span class="brand-dot"></span>
      <span class="product-name">Lumidrasc</span>
    </div>
    <p class="product-tagline">Culturally Immersive Language Learning Games</p>
    <div class="product-web">
      <svg width="120" height="10" viewBox="0 0 120 10" aria-hidden="true">
        <line x1="0" y1="5" x2="112" y2="5" stroke="var(--rule)" stroke-width="1.2"/>
        <circle cx="115" cy="5" r="3.5" fill="none" stroke="var(--rule)" stroke-width="1.2"/>
      </svg>
      <span class="product-url">www.lumidrasc.example</span>
      <svg width="120" height="10" viewBox="0 0 120 10" aria-hidden="true">
        <circle cx="5" cy="5" r="3.5" fill="none" stroke="var(--rule)" stroke-width="1.2"/>
        <line x1="8" y1="5" x2="120" y2="5" stroke="var(--rule)" stroke-width="1.2"/>
      </svg>
    </div>
  </section>

  <section class="card card--contact" aria-label="Contact side">
    <div class="company-brand">
      <span class="company-dot"></span>
      <span class="company-name">Quorvel</span>
    </div>
    <div class="contact">
      <p class="contact-name">Perry Hollins</p>
      <p class="contact-title">Founder &amp; CEO</p>
      <p class="contact-line">(555)-014-2736 | phollins@mailtrove.example</p>
    </div>
  </section>
</body>
</html>
```